Business Card Design for Marketing Firm

Looking for business card design for higher end marketing firm. Clean but impressionable/trendy. We are a marketing firm that represents manufacturers in the foodservice equipment and supply industry. Our customers are end users such has hotels, restaurants, country clubs, convention centers and casinos as well as distributors of restaurants supplies and equipment, and manufacturers of foodservice equipment and supplies.
Target Market(s)
Hotels, Restaurants, Supply & Equipment Distributors, Foodservice Manufacturers
Industry/Entity Type
Foodservice/Hospitality
Contact Information for Business Card
Name, Title, Contact Number, Email, Website, Social Media, Address
Requirements
Must have
- Clean & Simple but Serious and Impressionable

```html
<!DOCTYPE html>
<html lang="en">
<head>
<meta charset="utf-8">
<title>Meridian Service Reps — Business Cards</title>
<link rel="stylesheet" href="https://fonts.googleapis.com/css2?family=Outfit:wght@400;500;600&display=swap">
<style>
  :root {
    --navy: #2a2b73;
    --white: #ffffff;
    --paper: #ebebed;
    --ink: #1d1d2b;
    --stage: #ffffff;
  }
  * { box-sizing: border-box; margin: 0; padding: 0; }
  html, body { width: 1200px; height: 1200px; overflow: hidden; background: var(--stage); }
  body { position: relative; font-family: "Outfit", sans-serif; }

  .card { position: absolute; width: 508px; height: 311px; overflow: hidden; }
  .card--navy { background: var(--navy); color: var(--white); }
  .card--paper {
    background: linear-gradient(135deg, #e4e4e7 0%, #f2f2f4 55%, #e6e6e9 100%);
    color: var(--ink);
  }
  .row-top { top: 237px; }
  .row-bottom { top: 660px; }
  .col-front { left: 66px; }
  .col-back { left: 633px; }

  .front-name {
    position: absolute; right: 34px; bottom: 72px;
    font-weight: 500; font-size: 34px; line-height: 1.05; text-align: right;
    letter-spacing: 0.01em;
  }
  .card--paper .front-name { color: var(--navy); }

  .holder { position: absolute; left: 28px; top: 26px; }
  .holder-name { font-weight: 600; font-size: 17.5px; line-height: 1.1; }
  .card--paper .holder-name { color: var(--navy); }
  .holder-title { font-weight: 400; font-size: 14.5px; margin-top: 3px; }

  .brand {
    position: absolute; right: 28px; top: 64px;
    display: flex; align-items: center; gap: 6px;
    font-weight: 500; font-size: 11px; letter-spacing: 0.06em; text-transform: uppercase;
  }
  .card--paper .brand { color: var(--navy); }
  .brand-dot { width: 8px; height: 8px; border-radius: 50%; background: currentColor; }

  .contacts { position: absolute; left: 29px; top: 127px; list-style: none; }
  .contacts li {
    display: flex; align-items: center; height: 20px;
    font-weight: 500; font-size: 12.5px;
  }
  .contacts .icon { width: 14px; height: 14px; margin-right: 8px; flex: none; }
  .card--navy .icon { fill: var(--white); }
  .card--paper .icon { fill: var(--navy); }
  .social-mark { width: 10px; height: 10px; margin: 0 10px 0 2px; border-radius: 50%; flex: none; }
  .card--navy .social-mark { background: var(--white); }
  .card--paper .social-mark { background: var(--navy); }

  .address { position: absolute; left: 28px; top: 232px; font-size: 12px; line-height: 15.5px; }
  .website { position: absolute; left: 28px; top: 268px; font-size: 12.5px; font-weight: 500; }
</style>
</head>
<body>

  <!-- Navy set -->
  <section class="card card--navy row-top col-front" aria-label="Card front, navy">
    <p class="front-name">Meridian<br>Service Reps</p>
  </section>

  <section class="card card--navy row-top col-back" aria-label="Card back, navy">
    <div class="holder">
      <h2 class="holder-name">Calloway Renner</h2>
      <p class="holder-title">Chief Operation Marketing</p>
    </div>
    <div class="brand"><span class="brand-dot"></span>Meridian Service Reps</div>
    <ul class="contacts">
      <li><svg class="icon" viewBox="0 0 24 24"><path d="M6.6 10.8a15.1 15.1 0 0 0 6.6 6.6l2.2-2.2c.3-.3.7-.4 1-.2 1.1.4 2.3.6 3.6.6.6 0 1 .4 1 1V20c0 .6-.4 1-1 1A17 17 0 0 1 3 4c0-.6.4-1 1-1h3.5c.6 0 1 .4 1 1 0 1.3.2 2.5.6 3.6.1.3 0 .7-.2 1z"/></svg>+00 00 0000 0000</li>
      <li><svg class="icon" viewBox="0 0 24 24"><path d="M2 5h20v14H2z M3.5 6.5 12 13l8.5-6.5" /><path d="M2 5l10 8 10-8v14H2z" fill-opacity="1"/></svg>calloway.renner@meridianservice.com</li>
      <li><span class="social-mark"></span>@meridianreps</li>
    </ul>
    <p class="address">2250 Harbor Lane Suite 310 Laguna,<br>CA 92600 United States.</p>
    <p class="website">meridianservice.com</p>
  </section>

  <!-- Paper set -->
  <section class="card card--paper row-bottom col-front" aria-label="Card front, white paper">
    <p class="front-name">Meridian<br>Service Reps</p>
  </section>

  <section class="card card--paper row-bottom col-back" aria-label="Card back, white paper">
    <div class="holder">
      <h2 class="holder-name">Calloway Renner</h2>
      <p class="holder-title">Chief Operation Marketing</p>
    </div>
    <div class="brand"><span class="brand-dot"></span>Meridian Service Reps</div>
    <ul class="contacts">
      <li><svg class="icon" viewBox="0 0 24 24"><path d="M6.6 10.8a15.1 15.1 0 0 0 6.6 6.6l2.2-2.2c.3-.3.7-.4 1-.2 1.1.4 2.3.6 3.6.6.6 0 1 .4 1 1V20c0 .6-.4 1-1 1A17 17 0 0 1 3 4c0-.6.4-1 1-1h3.5c.6 0 1 .4 1 1 0 1.3.2 2.5.6 3.6.1.3 0 .7-.2 1z"/></svg>+00 00 0000 0000</li>
      <li><svg class="icon" viewBox="0 0 24 24"><path d="M2 5l10 8 10-8v14H2z"/></svg>calloway.renner@meridianservice.com</li>
      <li><span class="social-mark"></span>@meridianreps</li>
    </ul>
    <p class="address">2250 Harbor Lane Suite 310 Laguna,<br>CA 92600 United States.</p>
    <p class="website">meridianservice.com</p>
  </section>

</body>
</html>
```